Corporate Comedy Poster Brochure

I have designed an 10.75 by 15 flat one-sided poster/flyer to mail out for promoting my corporate comedy services. I don't think I did a bad job, but would love to see if someone can create something else for the same purpose, but with an expert hand and eye, as I am not a designer by trade. You should get a sense of it by the PSD example I provided.

FYI: My websites are:
www.paulvantrimm.com/corporate-comedian
www.gigsforstaffnights.com

Target Market(s)

Event Planners, Chambers of Commerce, Human Resources people who might be in charge of the company party, Golf Courses, Banquet Facilities, etc.

Industry/Entity Type

Entertainment Industry

Font styles to use
Sans Serif

Requirements
Must have
• Must have the textual content, headshot, and all logos that are in the PSD I provided.
• 10.75 inches by 15 inches at 300dpi.
• The PSD is on my Stashbox Cloud at :https://files.stashboxcloud.com/file/d/7Kq41mzvtp3WyhaR8cLn2JsXeQ60/view?usp=sharing
• I promise there is no virus or you know who's website to take down, :-)
Nice to have
• 1) Would be nice to have final in Photoshop, as I could then make adjustments easier. I don't know Illustrator well.
• 2) My motif is a poster for a show that is really a flyer promoting the fact that I perform shows. You can stick with this motif, or if you have a better motif, I am open to that.

```html
<!DOCTYPE html>
<html lang="en">
<head>
<meta charset="utf-8">
<title>Paul Van Trimm – Corporate Comedy Poster</title>
<link rel="stylesheet" href="https://fonts.googleapis.com/css2?family=Luckiest+Guy&family=Open+Sans:ital,wght@0,600;0,700;1,600&display=swap">
<style>
  :root {
    --red: #d1241f;
    --yellow: #f6c530;
    --white: #ffffff;
    --ink: #222222;
    --photo-a: #e8c9b2;
    --photo-b: #6d86a8;
  }
  * { margin: 0; padding: 0; box-sizing: border-box; }
  html, body { width: 857px; height: 1200px; overflow: hidden; background: var(--white); }
  .poster {
    position: relative; width: 857px; height: 1200px;
    background: var(--red); overflow: hidden;
    font-family: "Luckiest Guy", "Arial Black", sans-serif;
    color: var(--yellow);
  }
  .corner-band { position: absolute; left: 0; top: 0; width: 857px; height: 1200px; }
  .brand {
    position: absolute; left: 18px; top: 36px;
    display: flex; align-items: center; gap: 12px; white-space: nowrap;
  }
  .brand-mark { width: 72px; height: 72px; border-radius: 50%; background: var(--red); flex: none; }
  .brand-name { color: var(--red); font-size: 24px; line-height: 1.1; }
  .tagline {
    position: absolute; left: 390px; top: 60px; width: 440px;
    font-size: 30px; line-height: 1.15; font-weight: normal;
    transform: rotate(-6deg); transform-origin: left top;
  }
  .event-line {
    position: absolute; white-space: nowrap; font-size: 38px; line-height: 1;
    transform: rotate(-9deg); transform-origin: left center;
  }
  .event-line.l1 { left: 24px; top: 390px; }
  .event-line.l2 { left: 24px; top: 470px; }
  .event-line.l3 { left: 250px; top: 555px; }
  .event-line.l4 { left: 250px; top: 625px; }
  .testimonials {
    position: absolute; left: 645px; top: 470px; width: 192px;
    font-family: "Open Sans", Arial, sans-serif; font-style: italic; font-weight: 600;
    font-size: 14px; line-height: 1.3; text-align: right;
  }
  .testimonial + .testimonial { margin-top: 26px; }
  .testimonial cite { display: block; margin-top: 6px; font-size: 11px; }
  .headshot {
    position: absolute; left: 105px; top: 650px; width: 200px; height: 200px;
    border-radius: 50%; border: 6px solid var(--white);
    background: radial-gradient(circle at 50% 40%, var(--photo-a) 0 30%, var(--photo-b) 70%);
  }
  .performer-name {
    position: absolute; left: 20px; top: 868px; width: 370px; text-align: center;
    font-size: 36px; font-weight: normal; letter-spacing: 1px; white-space: nowrap;
    text-transform: uppercase;
  }
  .contact {
    position: absolute; left: 470px; top: 858px; width: 365px;
    font-size: 16px; line-height: 1.55; letter-spacing: 0.5px; text-align: right;
    text-transform: uppercase; white-space: nowrap;
  }
  .contact p + p { margin-top: 16px; }
  .partners {
    position: absolute; left: 40px; top: 940px; display: flex; gap: 18px; align-items: center;
  }
  .partner-badge { width: 92px; height: 42px; border-radius: 21px; background: var(--white); }
  .partner-badge.round { width: 54px; height: 54px; border-radius: 50%; }
  .clients {
    position: absolute; left: 0; top: 1057px; width: 857px; height: 143px;
    background: var(--white); padding: 20px 20px;
    display: flex; flex-direction: column; justify-content: space-between;
    font-family: "Open Sans", Arial, sans-serif; font-weight: 700; font-size: 17px;
  }
  .client-row { display: flex; justify-content: space-between; align-items: center; gap: 14px; }
  .client { white-space: nowrap; }
  .client.blue { color: #1f4e9c; }
  .client.red { color: #c8102e; }
  .client.green { color: #2f8a3b; }
  .client.magenta { color: #d6006e; }
  .client.orange { color: #e86a10; }
  .client.navy { color: #1b2a55; }
  .clients-note { width: 175px; font-size: 10px; line-height: 1.3; color: var(--ink); font-weight: 600; }
</style>
</head>
<body>
<main class="poster">
  <svg class="corner-band" viewBox="0 0 857 1200" aria-hidden="true">
    <polygon points="0,0 420,0 0,330" fill="#f6c530"/>
    <polygon points="857,1030 857,1057 660,1057" fill="#f6c530"/>
  </svg>

  <div class="brand">
    <span class="brand-mark"></span>
    <span class="brand-name">Paul Van Trimm<br>Comedy Night</span>
  </div>

  <h1 class="tagline">Hilarious entertainment for any corporate club or dinner event!</h1>

  <p class="event-line l1">Holiday Parties • Awards Banquets</p>
  <p class="event-line l2">Dinner Shows • Country Clubs</p>
  <p class="event-line l3">Community Shows</p>
  <p class="event-line l4">Fundraisers</p>

  <section class="testimonials">
    <blockquote class="testimonial">"Your show was AMAZING!!!! People were telling me for days how much fun they had and how great they thought you were."
      <cite>-Forwardly Insurance</cite></blockquote>
    <blockquote class="testimonial">"Paul, I can not tell you how well the evening went. This was the perfect first time comedy event."
      <cite>-Maple Ridge Country Club</cite></blockquote>
  </section>

  <div class="headshot" role="img" aria-label="Headshot of comedian Paul Van Trimm"></div>
  <h2 class="performer-name">Paul Van Trimm</h2>

  <section class="contact">
    <p>For more information:<br>Phone: 888-555-0142</p>
    <p>Website: www.paulvantrimm.com</p>
    <p>Email: comedian@paulvantrimm.com</p>
  </section>

  <div class="partners">
    <span class="partner-badge"></span>
    <span class="partner-badge round"></span>
    <span class="partner-badge"></span>
  </div>

  <section class="clients">
    <div class="client-row">
      <span class="client navy">Fieldstar</span>
      <span class="client green">GRN</span>
      <span class="client navy">Aerovia</span>
      <span class="client blue">Forwardly</span>
      <span class="client blue">Coverwell</span>
      <span class="client red">Freshway</span>
    </div>
    <div class="client-row">
      <span class="client red">Orchard Grill</span>
      <span class="client orange">BuildMart</span>
      <span class="client magenta">Telvo</span>
      <span class="client navy">Sea Pine Yacht Club</span>
      <span class="clients-note">And many other companies, country clubs and associations, both large and small.</span>
    </div>
  </section>
</main>
</body>
</html>
```